Study report design for interngovernmental organisation

We need a designer to provide a cover (front and back) to a prosaic governmental report. We need an introduction page, and just numbers and chapter designs throughout also. We would need the design in word format as we're incapable of working with anything else, and we still have a lot to edit! The topic is illicit financial flows, so ideas that come to mind: briefcases with money, anything that depicts money travelling across borders in an illicit manner.

Target Market(s)

Governments

Font styles to use
Serif
Sans Serif

Requirements
Must have
• A sober feel. Nothing too extravagant!

```html
<!DOCTYPE html>
<html lang="en">
<head>
<meta charset="utf-8">
<title>Illicit Financial Flows Report — Introduction Spread</title>
<link rel="stylesheet" href="https://fonts.googleapis.com/css2?family=Open+Sans:wght@400;600;700&display=swap">
<style>
  :root {
    --backdrop: #e4e4e4;
    --paper: #f7f7f7;
    --ink: #2b2b2b;
    --heading-blue: #1b5f9e;
    --box-blue: #1c6ebd;
    --band-dark: #3a3a3a;
    --band-mid: #8a8a8a;
    --white: #ffffff;
  }
  * { box-sizing: border-box; margin: 0; padding: 0; }
  html, body {
    width: 1200px; height: 912px; overflow: hidden;
    background: var(--backdrop);
    font-family: "Open Sans", Arial, sans-serif;
    color: var(--ink);
  }
  .spread {
    position: absolute; left: 60px; top: 60px;
    width: 1080px; height: 792px;
    display: flex;
    box-shadow: 0 6px 24px rgba(0,0,0,.18);
  }
  .page {
    position: relative; width: 540px; height: 792px;
    background: var(--paper); overflow: hidden;
    padding: 56px 44px 0 44px;
  }
  .page--left { border-right: 1px solid #d6d6d6; }
  .chapter-title {
    font-size: 22px; font-weight: 600; color: var(--heading-blue);
    margin-top: 8px;
  }
  .authors {
    font-size: 13px; font-weight: 600; color: var(--heading-blue);
    margin: 14px 0 22px;
  }
  .authors .joiner { color: var(--ink); }
  .section-heading {
    font-size: 13px; font-weight: 700; text-decoration: underline;
    margin: 0 0 7px;
  }
  .body-text {
    font-size: 9.2px; line-height: 1.36; text-align: justify;
    margin-bottom: 8px;
  }
  .bullets { list-style: none; margin: 4px 0 14px 14px; }
  .bullets li {
    position: relative; font-size: 9.2px; line-height: 1.36;
    padding-left: 22px; margin-bottom: 4px;
  }
  .bullets li::before {
    content: ""; position: absolute; left: 0; top: 4px;
    width: 4px; height: 4px; border-radius: 50%; background: var(--heading-blue);
  }
  .info-box {
    background: var(--box-blue); color: var(--white);
    margin: 18px -44px 0 18px; padding: 16px 40px 18px 22px;
  }
  .info-box__title { font-size: 11px; font-weight: 600; }
  .info-box__source { font-size: 10px; text-align: right; margin: 6px 0 14px; }
  .info-box .body-text { color: var(--white); font-size: 9.6px; }
  .page-number {
    position: absolute; font-size: 9px; color: var(--ink);
  }
  .page--left .page-number { left: 470px; top: 690px; }
  .page--right .page-number { right: 30px; top: 600px; }
  .footer-bands { position: absolute; left: 0; bottom: 0; }
</style>
</head>
<body>
<main class="spread">
  <section class="page page--left">
    <h1 class="chapter-title">1. Introduction</h1>
    <p class="authors">Mira HALDEN <span class="joiner">and</span> Tomas Verleye</p>

    <h2 class="section-heading">Illicit Financial Flows</h2>
    <p class="body-text">The term Illicit Financial Flows (IFFs) came into being in the 1990s; however, it only began to resonate with leaders, international organizations and other entities in the last ten years. A perfunctory glance at Searchly Trends best demonstrates the upward trajectory best; the term was first consulted via Searchly in 2007, and interest seemed to peak in September 2016 and May 2017, coinciding with the release of G20 Communiqués issued at the end of G20 Meetings in China and Germany, respectively.</p>
    <p class="body-text">Empirical research (OLI, 2008-2017; CCA/ERC, 2015; UNTDB, 2016) has laid the groundwork for these estimates, and provided theoretical underpinnings. The research suggests that there have been a significant amount of IFFs originating from developing countries, which undermine domestic resources for economic development. In particular, the Continental Panel on Illicit Financial Flows (2015) argued that Africa lost over 50 billion USD annually from illicit financial outflows, which exceed levels of Official Development Assistance to the continent. The UN Sustainable Development Goals specifically reference the significant threat posed by Illicit Financial Flows (IFFs), as captured in Goal 16 of the SDGs (16.4):</p>
    <p class="body-text">‘By 2030, significantly reduce illicit financial and arms flows, strengthen the recovery and return of stolen assets and combat all forms of organized crime’</p>
    <p class="body-text">However, IFFs should not be regarded as a problem of only developing countries. Considering that IFFs can be characterized as a reaction to the numerous offshore financial centers for tax evasion (Halvorsen, 2014), destabilize the global financial system (Global Finance Bank 2012), and are exploited to finance international organized crime and terrorist activities, IFFs should be considered as a global problem which necessitate urgent collective action.</p>

    <h2 class="section-heading">Trade mis-invoicing and IFFs</h2>
    <p class="body-text">The aforementioned empirical research identified trade mis-invoicing as a main channel of IFFs, illustrating significant discrepancies in bilateral trade statistics. Open Ledger Institute (OLI) has suggested that more than 80% of IFFs are accompanied by trade mis-invoicing. While such high figures have been criticized due to their estimation methods, empirical research (Brandt, 2012; Delorme and Kostas, 2014; Marsh and Oduya, 2016; Halden, 2018) support, at least, the presence of trade mis-invoicing in the trade discrepancy.</p>
    <p class="body-text">Another group of research (Lemaire, Ortiz &amp; Kwan, 2007; Sato and Kwan, 2016; Petrov, 2016) also revealed a significant amount of trade mis-invoicing based on the large value of</p>

    <span class="page-number">4</span>
    <svg class="footer-bands" width="540" height="80" viewBox="0 0 540 80" aria-hidden="true">
      <polygon points="0,14 540,2 540,20 0,32" fill="var(--band-mid)"/>
      <polygon points="0,44 540,30 540,52 0,66" fill="var(--band-dark)"/>
    </svg>
  </section>

  <section class="page page--right">
    <p class="body-text">trade, the unit prices of which were too abnormal compared to those of the same or similar goods. Case studies on money laundering (Regional Group on Money Laundering, 2012) and trade mis-invoicing (ICC, 2017) revealed in detail how the international trade system has been exploited for IFFs in collusion with the importer, exporter and/or financial intermediaries. Simplified examples are as follows:</p>
    <ul class="bullets">
      <li>over-invoiced imports to disguise capital flight as a form of trade payment,</li>
      <li>under-invoiced exports to conceal trade profit abroad (in a third-party country such as tax havens), and</li>
      <li>over-invoiced exports or under-invoiced imports to incorporate illicit proceeds into the domestic legal financial system.</li>
    </ul>

    <h2 class="section-heading">Customs and IFFs</h2>
    <p class="body-text">Many organizations and individuals have emphasized the importance of the role of Customs in combatting IFFs which exploit the international trade system (G20, 2016-2017; Regional Group on Money Laundering, 2012; OLI, 2015-2017). Customs administrations have a well-established pedigree with respect to combating cash smuggling, a subset of IFFs, and under-invoicing of imports, a subset of trade mis-invoicing. The traditional Customs’ roles of examination of ‘goods’ and collecting ‘revenues’ from trade continue to occupy the majority of their time and expertise; consequently, it is unsurprising that the realm of IFFs via trade mis-invoicing seems unfamiliar and remains unexplored territory for the vast majority of Customs administrations. As a consequence of their limited mandate, Customs may be unaware of the importance of trade mis-invoicing as a main channel of IFFs. According to an ICC survey (Lund and Abara, 2016), 62% of Customs administrations identified a ‘narrow or non-existing mandate’ as the biggest impediment in fighting against money laundering. The CDP Official Development Assistance to support countering IFFs via trade mis-invoicing (Box 1) gives an indication of the low level of interest from development partners in the role of Customs in combating IFFs.</p>

    <aside class="info-box">
      <h3 class="info-box__title">Box 1. How much aid goes into addressing illicit financial flows (IFFs)</h3>
      <p class="info-box__source">Provided by the CDP</p>
      <p class="body-text">Identifying the volume of Official Development Assistance (ODA) that is targeted towards addressing IFFs is difficult; projects targeting IFFs are not tagged as such in the Creditor Reporting System that the donors use to report their ODA spending. In their 2014 report, Illicit Financial Flows from Developing Countries: Measuring CDP Responses, the CDP identified that the Government and Civil Society sector was most likely to feature IFF or IFF related programmes. Spending in this area has declined in recent years from USD 14.5bn in 2011 to USD 11.9bn in 2016. This sector of ODA spending does not, however, cover assistance targeted towards trade, and so may not pick up projects that are specifically targeting</p>
    </aside>

    <span class="page-number">5</span>
    <svg class="footer-bands" width="540" height="120" viewBox="0 0 540 120" aria-hidden="true">
      <polygon points="0,40 400,24 380,62 0,78" fill="var(--band-dark)"/>
      <polygon points="0,90 540,70 540,100 0,120" fill="var(--band-dark)"/>
      <polygon points="410,22 540,16 540,52 395,58" fill="var(--box-blue)"/>
    </svg>
  </section>
</main>
</body>
</html>
```